Label for a Rye Bourbon bottle

This new brand will be a High Rye Bourbon Finished in Port Casks, the name of the brand will be Stone Hollow.
Proof will be 90, alc. by vol. 45% Volume 750 ML

Would like the look and feel not too feel as traditional as many bourbon labels out there, something that could appeal to a more adventurous drinker, not your grandfather.

Target Market(s)

Bourbon and Whiskey drinking aficionados

```html
<!DOCTYPE html>
<html lang="en">
<head>
<meta charset="utf-8">
<title>Stone Hollow — High Rye Bourbon Label</title>
<link rel="stylesheet" href="https://fonts.googleapis.com/css2?family=Josefin+Sans:wght@700&family=Oswald:wght@500&family=Montserrat:wght@400&display=swap">
<style>
  :root {
    --backdrop: #e8e3db;
    --label-black: #151515;
    --label-charcoal: #232323;
    --ink-white: #f4f2ee;
    --wood-tan: #c79a63;
  }
  * { margin: 0; padding: 0; box-sizing: border-box; }
  html, body {
    width: 1200px;
    height: 1021px;
    overflow: hidden;
    background: var(--backdrop);
  }
  .canvas {
    position: relative;
    width: 1200px;
    height: 1021px;
  }
  .label {
    position: absolute;
    left: 208px;
    top: 60px;
    width: 783px;
    height: 900px;
    border-radius: 22px;
    overflow: hidden;
    background: radial-gradient(ellipse at 40% 30%, var(--label-charcoal) 0%, var(--label-black) 75%);
    box-shadow: 0 2px 6px rgba(0,0,0,0.25);
  }
  .road-scene {
    position: absolute;
    left: 220px;
    top: 585px;
    right: 0;
    bottom: 0;
    background: linear-gradient(160deg, rgba(199,154,99,0) 0%, rgba(199,154,99,0.55) 45%, var(--wood-tan) 85%);
  }
  .brand-name {
    position: absolute;
    left: 0;
    right: 0;
    top: 148px;
    text-align: center;
    font-family: "Josefin Sans", sans-serif;
    font-weight: 700;
    color: var(--ink-white);
    text-transform: uppercase;
    line-height: 0.86;
    letter-spacing: 2px;
  }
  .brand-name span { display: block; }
  .brand-name .line-one { font-size: 172px; }
  .brand-name .line-two { font-size: 150px; margin-top: 22px; }
  .style-tag {
    position: absolute;
    left: 49px;
    top: 476px;
    width: 671px;
    height: 65px;
    border: 2.5px solid var(--ink-white);
    display: flex;
    align-items: center;
    justify-content: center;
    font-family: "Oswald", sans-serif;
    font-weight: 500;
    font-size: 35px;
    color: var(--ink-white);
    text-transform: uppercase;
    letter-spacing: 0.5px;
    white-space: nowrap;
  }
  .spec-lines {
    position: absolute;
    left: 52px;
    top: 738px;
    font-family: "Montserrat", sans-serif;
    font-size: 21px;
    line-height: 1.25;
    color: var(--ink-white);
  }
</style>
</head>
<body>
<main class="canvas">
  <section class="label" aria-label="Stone Hollow bourbon label">
    <div class="road-scene" role="img" aria-label="Illustration of a winding tan road running down to a wooden ground band"></div>
    <h1 class="brand-name">
      <span class="line-one">Stone</span>
      <span class="line-two">Hollow</span>
    </h1>
    <p class="style-tag">High Rye Bourbon Finished in Port Casks</p>
    <p class="spec-lines">alc. by vol.&nbsp; 45%<br>750 ML</p>
  </section>
</main>
</body>
</html>
```